Bref créative
Brindle Valley Property Owners Expo
Tuesday, April 24, 2012 6:00 - 8:30 pm
FREE Networking FREE Vendor Contacts FREE Hands-on Demos
The name of our org is the Brindle Valley Property Owners Guild (BVPOG).
This is our annual showcase--we have vendor tables, speakers and product demonstrations--much like a trade show.
Real Estate
Any real estate investor, rehabber, property manager or landlord.
Include this on card front:
National Marketing Expert, Dale Perkwith will show you the Money!
Fill your Vacancies--Attract Great Tenants!
We have a logo to use--how do I upload this?
On card front: Bring this card to show and be entered into drawing for $50 restaurant gift card.
On card back: Referred by:
On card back: BVPOG Property Owner Expo
Thornbury Elders Hall
5172 Larchmont Ave NE Canton OH
Network with the largest gathering of Real Estate Investors, Rehabbers, Landlords, and Property Managers in Brindle Valley.
FOOD! PRIZES!

```html
<!DOCTYPE html>
<html lang="en">
<head>
<meta charset="utf-8">
<title>Brindle Valley Property Owners Expo – Cards</title>
<link href="https://fonts.googleapis.com/css2?family=Source+Sans+3:ital,wght@0,400;0,600;0,700;0,900;1,600;1,700&display=swap" rel="stylesheet">
<style>
  :root {
    --stage: #3a3a3a;
    --navy: #1d2a44;
    --ink: #1a1a1a;
    --blue: #1f6db4;
    --bar-blue: #1f73bd;
    --paper: #f3f3f3;
    --mist: #d4d4d4;
    --panel: #c4c4c4;
    --band: #0d0d0d;
    --white: #ffffff;
    --sky-light: #ececec;
    --sky-mid: #b4b4b4;
    --tower-dark: #4a4a4a;
    --tower-blue: #8fa9c4;
    --tower-steel: #6f8aa6;
  }
  * { box-sizing: border-box; margin: 0; padding: 0; }
  html, body { width: 1200px; height: 857px; overflow: hidden; }
  body {
    background: var(--stage);
    font-family: "Source Sans 3", Arial, sans-serif;
    position: relative;
  }
  .card {
    position: absolute;
    top: 19px;
    width: 571px;
    height: 814px;
    overflow: hidden;
    box-shadow: 0 4px 14px rgba(0,0,0,.45);
  }
  .card--front {
    left: 19px;
    background: linear-gradient(180deg, var(--white) 0%, var(--paper) 18%, var(--mist) 40%, #bdbdbd 100%);
  }
  .card--back { left: 610px; background: var(--white); }

  /* Org mark */
  .org-mark { position: absolute; display: flex; align-items: center; gap: 10px; }
  .org-mark__dot { border-radius: 50%; background: var(--navy); flex: none; }
  .org-mark__name { font-weight: 700; color: var(--navy); }

  .front__mark { left: 30px; top: 72px; }
  .front__mark .org-mark__dot { width: 66px; height: 66px; }
  .front__mark .org-mark__name { font-size: 28px; }

  .front__title {
    position: absolute; left: 209px; top: 70px; width: 350px;
    font-weight: 900; font-size: 29px; line-height: 31px;
    color: var(--navy); text-transform: uppercase;
  }
  .front__date {
    position: absolute; left: 209px; top: 136px;
    font-size: 17px; font-weight: 600; color: var(--blue);
  }
  .front__speaker {
    position: absolute; left: 34px; top: 244px;
    font-size: 21px; line-height: 30px; color: var(--ink);
  }
  .front__speaker em { font-weight: 700; }
  .front__bar {
    position: absolute; left: 0; top: 314px; width: 100%; height: 32px;
    background: var(--bar-blue);
    display: flex; align-items: center; justify-content: center; gap: 14px;
    color: var(--white); font-weight: 700; font-size: 19px;
  }
  .front__art {
    position: absolute; left: 0; top: 346px; width: 100%; height: 403px;
    background:
      radial-gradient(ellipse 45% 55% at 28% 72%, rgba(40,40,40,.55) 0%, rgba(40,40,40,0) 100%),
      radial-gradient(ellipse 40% 60% at 78% 45%, rgba(255,255,255,.55) 0%, rgba(255,255,255,0) 100%),
      radial-gradient(ellipse 35% 40% at 12% 95%, rgba(90,90,90,.6) 0%, rgba(90,90,90,0) 100%),
      linear-gradient(180deg, var(--sky-light) 0%, #cfcfcf 30%, var(--sky-mid) 60%, var(--tower-dark) 100%);
  }
  .front__band {
    position: absolute; left: 0; top: 749px; width: 100%; height: 65px;
    background: var(--band); color: var(--white);
    text-align: center; font-size: 17px; line-height: 24px; padding-top: 9px;
  }
  .front__band strong { font-weight: 700; font-size: 18px; }

  /* Back */
  .back__referred {
    position: absolute; left: 40px; top: 26px;
    font-size: 24px; font-weight: 700; color: var(--ink);
  }
  .back__mark { left: 40px; top: 94px; }
  .back__mark .org-mark__dot { width: 40px; height: 40px; }
  .back__mark .org-mark__name { font-size: 19px; }
  .back__venue {
    position: absolute; left: 158px; top: 76px;
    font-size: 18px; line-height: 28px; color: var(--ink);
  }
  .back__venue strong { font-weight: 700; }
  .back__art {
    position: absolute; left: 0; top: 197px; width: 100%; height: 264px;
    background:
      radial-gradient(ellipse 30% 45% at 28% 38%, rgba(70,80,95,.35) 0%, rgba(70,80,95,0) 100%),
      radial-gradient(ellipse 30% 45% at 62% 38%, rgba(70,80,95,.3) 0%, rgba(70,80,95,0) 100%),
      radial-gradient(ellipse 55% 45% at 70% 100%, rgba(111,138,166,.85) 0%, rgba(111,138,166,0) 100%),
      radial-gradient(ellipse 30% 50% at 8% 100%, rgba(143,169,196,.8) 0%, rgba(143,169,196,0) 100%),
      linear-gradient(180deg, var(--white) 0%, #eef2f6 45%, var(--tower-blue) 100%);
  }
  .back__panel {
    position: absolute; left: 0; top: 461px; width: 100%; height: 353px;
    background: linear-gradient(180deg, #cfcfcf 0%, var(--panel) 100%);
    padding: 44px 40px 0;
    color: var(--ink);
  }
  .back__lead { font-size: 23px; line-height: 30px; }
  .back__audience {
    font-size: 32px; line-height: 40px; font-weight: 600; color: var(--blue);
    margin-top: 6px;
  }
  .back__where { font-size: 23px; line-height: 30px; margin-top: 4px; }
  .back__perks { font-size: 31px; font-weight: 700; margin-top: 48px; }
</style>
</head>
<body>
  <section class="card card--front">
    <div class="org-mark front__mark">
      <span class="org-mark__dot"></span>
      <span class="org-mark__name">BVPOG</span>
    </div>
    <h1 class="front__title">Brindle Valley Property Owners Expo</h1>
    <p class="front__date">Tuesday, April 24, 2012 6:00 - 8:30 pm</p>
    <p class="front__speaker">National Marketing Expert,<br><em>Dale Perkwith will show you the Money!</em></p>
    <div class="front__bar">
      <span>Fill your Vacancies</span>
      <svg width="12" height="14" viewBox="0 0 12 14" aria-hidden="true"><path d="M1 1 L11 7 L1 13 Z" fill="#ffffff"/></svg>
      <span>Attract Great Tenants!</span>
    </div>
    <div class="front__art" role="img" aria-label="Grey city skyline with two business people shaking hands"></div>
    <p class="front__band">Bring this card to show and be entered into drawing for<br><strong>$50 restaurant gift card</strong></p>
  </section>

  <section class="card card--back">
    <p class="back__referred">Referred by:</p>
    <div class="org-mark back__mark">
      <span class="org-mark__dot"></span>
      <span class="org-mark__name">BVPOG</span>
    </div>
    <p class="back__venue"><strong>BVPOG Property Owner Expo</strong><br>Thornbury Elders Hall<br>5172 Larchmont Ave NE Canton OH</p>
    <div class="back__art" role="img" aria-label="Two businessmen shaking hands in front of blue city towers"></div>
    <div class="back__panel">
      <p class="back__lead">Network with the largest gathering of</p>
      <p class="back__audience">Real Estate Investors, Rehabbers,<br>Landlords, &amp; Property Managers</p>
      <p class="back__where">in Brindle Valley.</p>
      <p class="back__perks">FOOD! PRIZES!</p>
    </div>
  </section>
</body>
</html>
```